Window Tinting Website Design

We are working with a Window Tinting company in California. They do commercial, residential, and automotive tint.

Some websites for inspiration:
https://www.velmoshadez.com/
https://www.qpridegleam.com/
https://drobfinishx.com/

Thank you for taking the time to consider designing a website for us. We are web developers based in Stockton, CA, USA. Most of our projects go through the same process. Understanding this process may help you win a project with us. We custom-code all of our websites in-house. We don’t have any requirements as to what tools you use for your design, but we ask that you follow these guidelines.

IMAGES:
If you use any images or icons in the design, we ask that you have a link to the asset so we can purchase the image/icon. Most of the designs we submit do not have the customer’s images on them unless they have some great images. Be creative; show us the feeling you are trying to portray with your image choices. Use any royalty-free site you choose. We subscribe to Brenlo and mainly use their images, but we can purchase images outside of Brenlo. PLEASE NOTE: we will not submit designs to clients with watermarks on the images.

FONTS:
We ask that you identify the fonts you’re using in the design. This can be done in a message if you want. We typically use Google Fonts and Brenlo Fonts.

CONTENT:
We're always open to different content and ideas. We often submit designs with stock images so the client can see our vision. We typically take pictures after the website launch to use their images with our vision. Lorem Ipsum is fine for paragraphs, but we ask that you make the Headers with correct English. We want to be able to show the vision and identify the sections of the website.

INSPIRATION:
We typically add a couple of links in the brief of websites we like to help you get started in your design.

REVISIONS:
We do not often ask for revisions of the designs unless we see something in the design that may not appeal to the client. If there are slight changes that we want to make, we do that in the development process.

FEEDBACK:
We rarely give feedback on designs during the design process. We are working on many website projects and do not have the time to provide feedback. We usually respond if your request is well thought out and asks specific questions, but a note asking “feedback, please” usually goes unanswered.

```html
<!DOCTYPE html>
<html lang="en">
<head>
<meta charset="utf-8">
<title>Clearview Shade Co – Window Tinting</title>
<link href="https://fonts.googleapis.com/css2?family=Poppins:ital,wght@0,400;0,500;0,600;0,700;1,400&display=swap" rel="stylesheet">
<style>
:root{
  --stage:#4b6e8d;
  --brand-blue:#4b6e8d;
  --brand-red:#c8102e;
  --ink:#1f1f1f;
  --muted:#6b6b6b;
  --dark:#333333;
  --paper:#ffffff;
  --field:#ececec;
}
*{margin:0;padding:0;box-sizing:border-box}
html,body{width:893px;height:1200px;overflow:hidden}
body{background:var(--stage);font-family:"Poppins",sans-serif;color:var(--ink);position:relative}
.abs{position:absolute}
.page{position:absolute;top:74px;background:var(--paper);border-radius:10px;overflow:hidden;box-shadow:0 6px 24px rgba(0,0,0,.18)}
.page--left{left:12px;width:410px;height:1048px}
.page--right{left:432px;width:449px;height:1048px}

/* nav */
.brand{display:flex;align-items:center;gap:3px;font-weight:700;color:var(--brand-red);font-size:6.5px;line-height:1;white-space:nowrap}
.brand--header{font-size:4.6px;gap:2px}
.brand__dot{width:7px;height:7px;border-radius:50%;background:var(--brand-red);flex:none}
.brand--header .brand__dot{width:5px;height:5px}
.nav{display:flex;gap:8px;font-size:4.3px;color:var(--ink);white-space:nowrap}
.btn{background:var(--brand-red);color:#fff;font-weight:600;border-radius:4px;display:flex;align-items:center;justify-content:center;text-align:center;white-space:nowrap}

/* hero */
.hero{border-radius:8px;overflow:hidden;background:linear-gradient(120deg,#5d86b5 0%,#8fb0d6 35%,#3d5f86 60%,#1f3551 100%)}
.hero__title{color:#fff;font-weight:700;font-size:13.5px;line-height:17px}
.hero__lede{color:#eef3f8;font-size:4.3px;line-height:6.5px;width:150px}
.stats{background:#fff;border-radius:5px;box-shadow:0 3px 10px rgba(0,0,0,.12);display:flex;align-items:center;justify-content:space-around;padding:0 8px}
.stat{text-align:center;flex:1;border-right:1px solid #d9d9d9}
.stat:last-child{border-right:none}
.stat__num{color:var(--brand-blue);font-weight:600;font-size:13px;line-height:15px}
.stat__label{color:var(--brand-blue);font-size:3.8px;line-height:5px}

/* about */
.photo{border-radius:5px}
.eyebrow{font-size:3.6px;color:var(--brand-blue)}
.h-sm{font-weight:600;font-size:8px}
.body-xs{font-size:4.1px;line-height:5.8px;color:#333;text-align:justify}

/* services */
.services{background:var(--dark);border-radius:38px 38px 0 0}
.section-title{font-weight:600;font-size:8.5px;text-align:center}
.service__img{width:113px;height:70px;border-radius:4px}
.service__title{color:#fff;font-weight:600;font-size:6px}
.service__text{color:#d8d8d8;font-size:3.7px;line-height:5.6px;text-align:justify;width:102px}
.btn--xs{font-size:3.6px;width:37px;height:8px;border-radius:2px}
.banner{border-radius:7px;background:linear-gradient(135deg,#2e5a9c 0%,#6d9bd6 40%,#9fc0e6 55%,#2c5591 100%);color:#fff;font-weight:600;font-size:8.2px;line-height:13px;text-align:center;display:flex;align-items:center;justify-content:center}

/* process */
.step{background:var(--brand-blue);border-radius:6px;color:#fff;font-size:5.6px;line-height:7.5px;text-align:center;display:flex;align-items:center;justify-content:center;padding-top:6px}
.step__num{position:absolute;left:4px;top:4px;width:8px;height:8px;border-radius:50%;background:#fff;color:var(--brand-blue);font-size:4.5px;font-weight:600;display:flex;align-items:center;justify-content:center}

/* testimonials */
.testimonials{background:linear-gradient(120deg,#4f4f4f 0%,#3e3e3e 55%,#4b6277 100%)}
.quote-card{background:rgba(45,45,45,.92);display:flex}
.avatar{width:14px;height:14px;border-radius:50%;background:#c9b8a3}
.quote{color:#e4e4e4;font-style:italic;font-size:3.7px;line-height:5.6px;width:130px}
.dot{width:3px;height:3px;border-radius:50%;background:#9a9a9a}
.dot--on{background:var(--brand-red)}

/* form */
.field{background:var(--field);border:1px solid #e0e0e0;border-radius:3px;font-size:3.8px;font-style:italic;color:#a0a0a0;padding:7px 9px}

/* footer */
.footer{background:var(--brand-blue);color:#fff}
.foot__head{font-weight:600;font-size:4.6px}
.foot__list{list-style:none;font-size:3.6px;line-height:8.5px;white-space:nowrap}
.social{display:flex;gap:5px}
.social span{width:6px;height:6px;border-radius:50%;border:1px solid #fff}
</style>
</head>
<body>

<!-- Left page -->
<section class="page page--left">
  <div class="abs brand brand--header" style="left:26px;top:22px">
    <span class="brand__dot"></span>Clearview Shade Co
  </div>
  <nav class="abs nav" style="left:100px;top:22px">
    <span>Commercial Tinting</span><span>Residental Tinting</span><span>Automotive Tinting</span><span>Testimonials</span><span>Gallery</span><span>About Us</span>
  </nav>
  <div class="abs btn" style="left:328px;top:15px;width:55px;height:20px;font-size:4.3px">Contact Us</div>

  <div class="abs hero" style="left:9px;top:40px;width:391px;height:162px" role="img" aria-label="Upward view of glass skyscrapers against a blue sky"></div>
  <h1 class="abs hero__title" style="left:32px;top:72px">Premium Window Film<br>&amp; Paint Protection<br>Solutions</h1>
  <p class="abs hero__lede" style="left:32px;top:130px">Choose us to transform your space, as we bring unrivaled quality, expertise, and customer satisfaction to every project.</p>
  <div class="abs btn" style="left:32px;top:155px;width:55px;height:14px;font-size:4px">Get Your Quote</div>

  <div class="abs stats" style="left:148px;top:178px;width:233px;height:44px">
    <div class="stat"><div class="stat__num">3</div><div class="stat__label">Years<br>Experience</div></div>
    <div class="stat"><div class="stat__num">50</div><div class="stat__label">Professional<br>Worker</div></div>
    <div class="stat"><div class="stat__num">100+</div><div class="stat__label">Projects<br>Done</div></div>
    <div class="stat"><div class="stat__num">200+</div><div class="stat__label">Positive<br>Reviews</div></div>
  </div>

  <div class="abs photo" style="left:28px;top:257px;width:174px;height:122px;background:linear-gradient(135deg,#9fb1c2,#5a6977 55%,#2f3a44)" role="img" aria-label="Installer in a hard hat fitting a large window frame"></div>
  <p class="abs eyebrow" style="left:218px;top:276px">About Us</p>
  <h2 class="abs h-sm" style="left:218px;top:284px">Based on Experience</h2>
  <p class="abs body-xs" style="left:218px;top:302px;width:142px">Lorem ipsum dolor sit amet consectetur. Leo convallis mattis aliquam urna. Id dui pellentesque cras dictumst nibh adipiscing lorem. Sem magnis est montes netus integer nullam. Id nulla sagittis elementum faucibus. Porttitor feugiat ipsum elit sit id pretium euismod. In erat amet mauris eget. Egestas facilisis cursus pellentesque tempus sapien commodo amet volutpat et. Duis massa aliquam tempus mattis ac. Faucibus viverra in eros urna. Pretium malesuada fames ultrices erat eu odio est auctor quis. Scelerisque pretium egestas arcu aliquam.</p>

  <div class="abs services" style="left:9px;top:427px;width:391px;height:513px"></div>
  <h2 class="abs section-title" style="left:9px;top:460px;width:391px;color:#fff">Our Services</h2>

  <div class="abs service__img" style="left:28px;top:493px;background:linear-gradient(135deg,#c7d3a8,#f1ece2 60%,#e7dccb)" role="img" aria-label="Technician applying film to a home window"></div>
  <div class="abs service__img" style="left:148px;top:493px;background:linear-gradient(135deg,#5d7487,#9bb0bf 50%,#3e4f5d)" role="img" aria-label="Workers on the glass facade of an office building"></div>
  <div class="abs service__img" style="left:268px;top:493px;background:linear-gradient(135deg,#e2e0dc,#d6a52c 45%,#35383b)" role="img" aria-label="Technician heat-shrinking tint film on a car window"></div>

  <h3 class="abs service__title" style="left:34px;top:578px">Residential Window Tinting</h3>
  <h3 class="abs service__title" style="left:153px;top:578px">Commercial Window Tinting</h3>
  <h3 class="abs service__title" style="left:273px;top:578px">Automotive Window Tinting</h3>
  <p class="abs service__text" style="left:34px;top:592px">Improve your home's energy efficiency, enhance privacy, and protect your furniture and belongings from harmful UV rays. Enjoy a cooler and more comfortable living environment while reducing your energy bills.</p>
  <p class="abs service__text" style="left:153px;top:592px">Enhance your business space with our commercial window tinting service. Reduce heat gain, improve energy efficiency, and create a more comfortable working environment for your employees and clients.</p>
  <p class="abs service__text" style="left:273px;top:592px">Upgrade your vehicle's style, comfort, and privacy with our automotive window tinting service. Protect yourself and your passengers from harmful UV rays, reduce heat and glare, and add a sleek, customized look to your car.</p>
  <div class="abs btn btn--xs" style="left:34px;top:641px">Read More ››</div>
  <div class="abs btn btn--xs" style="left:153px;top:641px">Read More ››</div>
  <div class="abs btn btn--xs" style="left:273px;top:641px">Read More ››</div>

  <div class="abs service__img" style="left:28px;top:666px;background:linear-gradient(135deg,#2f5d9c,#a9c4e3 45%,#294f86)" role="img" aria-label="Reflective blue glass building facade"></div>
  <div class="abs service__img" style="left:148px;top:666px;background:linear-gradient(180deg,#2f6fc4,#d7d2c6 50%,#8a8478)" role="img" aria-label="Classic stone building with many windows"></div>
  <div class="abs service__img" style="left:268px;top:666px;background:linear-gradient(135deg,#c9a57a,#8a6a45 50%,#3b2c22)" role="img" aria-label="Cafe window with a custom printed graphic"></div>

  <h3 class="abs service__title" style="left:34px;top:751px">UV Protection</h3>
  <h3 class="abs service__title" style="left:153px;top:751px">Solar Heat Reduction</h3>
  <h3 class="abs service__title" style="left:273px;top:751px">Custom Designs and Graphics</h3>
  <p class="abs service__text" style="left:34px;top:766px">Protect yourself, your loved ones, and your belongings from the damaging effects of harmful ultraviolet (UV) rays. Our window tinting films block up to 99% of UV radiation, safeguarding from fading and sun damage.</p>
  <p class="abs service__text" style="left:153px;top:766px">High-quality films that reduce solar heat gain. By blocking a substantial amount of the sun's infrared rays, our tints keep your interiors cooler, reducing the need for excessive air conditioning and lowering energy costs.</p>
  <p class="abs service__text" style="left:273px;top:766px">Express your creativity and brand identity with our custom window tinting designs and graphics. Whether you want to display your company logo, add decorative patterns, or create a unique visual appeal.</p>
  <div class="abs btn btn--xs" style="left:34px;top:815px">Read More ››</div>
  <div class="abs btn btn--xs" style="left:153px;top:815px">Read More ››</div>
  <div class="abs btn btn--xs" style="left:273px;top:815px">Read More ››</div>

  <div class="abs banner" style="left:28px;top:881px;width:354px;height:133px" role="img" aria-label="Blue glass curtain wall reflecting clouds">High Quality and Experienced Worker<br>For The Perfection</div>
</section>

<!-- Right page -->
<section class="page page--right">
  <h2 class="abs h-sm" style="left:38px;top:42px;font-size:8.5px;line-height:12px">How We Work<br>On Your Project</h2>

  <div class="abs step" style="left:130px;top:41px;width:91px;height:48px"><span class="step__num">1</span>Consultation</div>
  <div class="abs step" style="left:229px;top:41px;width:91px;height:48px"><span class="step__num">2</span>Assessment<br>and Evaluation</div>
  <div class="abs step" style="left:328px;top:41px;width:91px;height:48px"><span class="step__num">3</span>Customized<br>Solution Proposal</div>
  <div class="abs step" style="left:130px;top:96px;width:91px;height:48px"><span class="step__num">4</span>Scheduling<br>the Installation</div>
  <div class="abs step" style="left:229px;top:96px;width:91px;height:48px"><span class="step__num">5</span>Post-Installation<br>Care &amp; Guidelines</div>
  <div class="abs step" style="left:328px;top:96px;width:91px;height:48px"><span class="step__num">6</span>Follow-Up &amp;<br>Customer Support</div>

  <h2 class="abs section-title" style="left:0;top:199px;width:449px">Our Project</h2>
  <div class="abs" style="left:31px;top:225px;width:387px;height:148px">
    <div class="abs" style="left:0;top:0;width:92px;height:80px;background:linear-gradient(135deg,#e8ece9,#4f7a55 50%,#cfd6d2)" role="img" aria-label="Tinted windows in a bright interior"></div>
    <div class="abs" style="left:92px;top:0;width:131px;height:80px;background:linear-gradient(135deg,#2d2d2d,#c8141c 50%,#e9e9e9)" role="img" aria-label="Front of a red sedan"></div>
    <div class="abs" style="left:0;top:80px;width:123px;height:68px;background:linear-gradient(135deg,#6a6a6a,#d21a1f 55%,#8c1014)" role="img" aria-label="Classic red car with tinted windows"></div>
    <div class="abs" style="left:123px;top:80px;width:100px;height:68px;background:linear-gradient(180deg,#f3f1ec,#d9d3c7 60%,#b98f63)" role="img" aria-label="Empty room with a large window"></div>
    <div class="abs" style="left:223px;top:0;width:98px;height:148px;background:linear-gradient(180deg,#d8d8d6,#3c4a55 45%,#c9c6c0)" role="img" aria-label="Glass storefront of a commercial building"></div>
    <div class="abs" style="left:321px;top:0;width:66px;height:148px;background:linear-gradient(135deg,#4a4a4a,#b77f67 45%,#7a1820 80%)" role="img" aria-label="Hands smoothing tint film onto a car window"></div>
  </div>
  <div class="abs btn" style="left:195px;top:392px;width:60px;height:15px;font-size:4px">See More ››</div>

  <div class="abs testimonials" style="left:10px;top:457px;width:428px;height:223px"></div>
  <h2 class="abs section-title" style="left:0;top:474px;width:449px;color:#fff">Testimonials</h2>
  <div class="abs quote-card" style="left:31px;top:508px;width:387px;height:134px">
    <div style="width:190px;height:134px;background:linear-gradient(135deg,#3a3a3a,#c8141c 50%,#5c5c5c)" role="img" aria-label="Red sedan parked in a showroom"></div>
  </div>
  <div class="abs avatar" style="left:245px;top:542px"></div>
  <p class="abs" style="left:264px;top:543px;font-size:4.5px;font-weight:500;color:#fff">Dalen Ostrow</p>
  <p class="abs" style="left:264px;top:550px;font-size:3.6px;color:#bdbdbd">California</p>
  <p class="abs quote" style="left:245px;top:565px">"Lorem ipsum dolor sit amet consectetur. Vitae proin in cursus diam. Facilisis magnis consectetur turpis tincidunt. Morbi viverra elementum morbi at volutpat facilisis. Massa vulputate ullamcorper pulvinar ultrices aenean facilisi nisl adipiscing rhoncus. Pellentesque facilisi nunc ornare enim turpis. Vestibulum quis diam sollicitudin malesuada risus at."</p>
  <div class="abs" style="left:198px;top:665px;display:flex;gap:5px">
    <span class="dot dot--on"></span><span class="dot"></span><span class="dot"></span><span class="dot"></span>
  </div>

  <h2 class="abs h-sm" style="left:31px;top:737px">Tell Us Your Project</h2>
  <div class="abs field" style="left:30px;top:760px;width:158px;height:22px">Your Name</div>
  <div class="abs field" style="left:30px;top:788px;width:158px;height:22px">Email</div>
  <div class="abs field" style="left:30px;top:816px;width:158px;height:22px">Phone Number</div>
  <div class="abs field" style="left:195px;top:760px;width:223px;height:78px">Write your message here</div>
  <div class="abs btn" style="left:357px;top:855px;width:60px;height:15px;font-size:4px">Send</div>

  <footer class="abs footer" style="left:10px;top:923px;width:428px;height:114px">
    <div class="abs brand" style="left:33px;top:32px;color:#fff;font-size:9px;gap:4px"><span class="brand__dot" style="background:#fff;width:9px;height:9px"></span>Clearview Shade Co</div>
    <p class="abs" style="left:20px;top:69px;width:115px;font-size:3.6px;line-height:5.2px">Lorem ipsum dolor sit amet consectetur. Vitae iaculis fermentum lacinia cras at congue sit. In ultrices nunc cras rhoncus turpis pharetra penatibus sit nisi.</p>

    <p class="abs foot__head" style="left:160px;top:12px">Our Services</p>
    <ul class="abs foot__list" style="left:160px;top:22px">
      <li>Residental Window Tinting</li><li>Commercial Window Tinting</li><li>Automotive Window Tinting</li><li>UV Protection</li><li>Solar Heat Reduction</li><li>Custom Design and Graphics</li>
    </ul>

    <p class="abs foot__head" style="left:265px;top:12px">Support</p>
    <ul class="abs foot__list" style="left:265px;top:22px">
      <li>Community</li><li>Forums</li><li>Terms &amp; Condition</li><li>Privacy Policy</li>
    </ul>
    <div class="abs social" style="left:265px;top:85px"><span></span><span></span><span></span><span></span><span></span></div>

    <p class="abs foot__head" style="left:350px;top:12px">Company</p>
    <ul class="abs foot__list" style="left:350px;top:22px">
      <li>About Us</li><li>Careers</li><li>Contact</li>
    </ul>
    <svg class="abs" style="left:352px;top:74px" width="5" height="7" viewBox="0 0 10 14" aria-hidden="true"><path d="M5 13s4-5 4-8a4 4 0 1 0-8 0c0 3 4 8 4 8z" fill="none" stroke="#fff" stroke-width="1.4"/><circle cx="5" cy="5" r="1.5" fill="#fff"/></svg>
    <p class="abs" style="left:362px;top:74px;font-size:3.6px;line-height:5px;white-space:nowrap">482 Harbor Lane<br>Suite 210<br>Fresno, CA 93701</p>
  </footer>
</section>

</body>
</html>
```